Meadowbrook Holdings Website Design

We have been redeveloping our website already and are quite happy with the content, but the design needs to be better:
https://trelvan-site.examplehost.net/

Pages, content, concept etc. Can all be taken from the redeveloped website.
The farmer can register and edit/view their profile, subscribe and these pages need to be designed better as well as contact, about, pricing, tos, privacy and a page with example portlets.

We need a website to appeal to farmers, investors and retiring farmers.

The design should be clean and a little country.

We don't want any repeat designs that some may submit to every project and has no respect for the project brief, so please don't submit them.

Target Market(s)

farmers, investors, retirees

Industry/Entity Type

Farming

Number of Pages Required

5+ page

Colors

Designer to choose colors to be used in the design.

Requirements
Must have
• Nice, clean modern design that is appealing
• Profile page laid out nicely

```html
<!DOCTYPE html>
<html lang="en">
<head>
<meta charset="utf-8">
<title>Farmer Profile – Meadowbrook Holdings</title>
<link href="https://fonts.googleapis.com/css2?family=Poppins:wght@500;600&family=Roboto:wght@400;500&display=swap" rel="stylesheet">
<style>
:root{
  --green:#3aa53c;
  --green-dark:#2e7d32;
  --orange:#f5890f;
  --ink:#222;
  --text:#444;
  --muted:#666;
  --line:#e2e2e2;
  --band:#f1f1f1;
  --footer:#3a3a3a;
  --footer-text:#cfcfcf;
}
*{margin:0;padding:0;box-sizing:border-box}
html,body{width:793px;height:1200px;overflow:hidden;background:#fff}
body{font-family:Roboto,sans-serif;color:var(--text);position:relative}
.site-header{position:absolute;top:0;left:0;width:793px;height:62px;background:#f6f6f6;z-index:2}
.brand-badge{position:absolute;left:52px;top:0;width:72px;height:80px;background:#fff;border-radius:0 0 36px 36px;display:flex;align-items:center;justify-content:center}
.brand-badge span{width:34px;height:34px;border-radius:50%;background:var(--green-dark)}
.main-nav{position:absolute;left:149px;top:25px;display:flex;gap:15px;font-size:10px;font-weight:500;color:var(--ink)}
.sign-in{position:absolute;right:63px;top:25px;font-size:10px;font-weight:500;color:var(--orange);display:flex;align-items:center;gap:4px}
.hero{position:absolute;top:62px;left:0;width:793px;height:169px;background:linear-gradient(90deg,#4f6040,#2f3a2a 40%,#4a6a8a 75%,#5b7d46);display:flex;align-items:center;justify-content:center}
.hero h1{font-family:Poppins,sans-serif;font-weight:600;font-size:27px;color:#fff}
.breadcrumb{position:absolute;top:231px;left:0;width:793px;height:26px;background:var(--band);font-size:11.5px;padding:6px 0 0 49px;color:var(--text)}
.breadcrumb a{color:var(--green);text-decoration:none}
.profile-photo{position:absolute;left:49px;top:288px;width:160px;height:160px;background:linear-gradient(135deg,#8a7a62,#b9ab8e 50%,#5f6e3a)}
.profile-info{position:absolute;left:240px;top:285px}
.profile-info h2{font-family:Poppins,sans-serif;font-weight:500;font-size:16px;color:var(--ink);margin-bottom:8px}
.field{font-size:10.5px;font-weight:500;color:#333;line-height:19.6px;white-space:nowrap}
.field span{font-weight:400;font-size:9px;color:var(--muted)}
.divider{position:absolute;left:49px;width:695px;height:1px;background:var(--line)}
.col{position:absolute;top:507px}
.col h3{font-size:11.5px;font-weight:500;color:#333;margin-bottom:9px}
.col ul{list-style:none}
.col li{font-size:9.5px;color:var(--muted);height:19.6px;display:flex;align-items:center;gap:6px}
.badge{width:13px;height:13px;border-radius:50%;background:var(--green);color:#fff;font-size:8px;font-style:normal;display:inline-flex;align-items:center;justify-content:center}
.col .other{margin-top:6px}
.options{position:absolute;left:49px;top:867px}
.footer{position:absolute;top:975px;left:0;width:793px;height:225px;background:var(--footer);color:var(--footer-text)}
.footer h4{font-size:11px;font-weight:500;color:#fff;position:absolute;top:24px}
.post{position:absolute;left:49px;display:flex;gap:12px}
.date{width:41px;height:41px;background:var(--green);color:#fff;text-align:center;font-size:7.5px;padding-top:3px}
.date b{display:block;font-size:19px;font-weight:500;line-height:20px}
.post p{font-size:11px;color:#fff;line-height:14.5px;width:180px}
.post small{display:block;font-size:9px;color:#aaa;margin-top:3px}
.vline{position:absolute;top:22px;width:1px;height:112px;background:#4c4c4c}
.newsletter p{position:absolute;left:328px;top:46px;width:220px;font-size:9.5px;line-height:14.5px;color:#bbb}
.email{position:absolute;left:328px;top:87px;width:219px;height:24px;border-radius:12px;background:#fff;font-size:9px;color:#888;padding:6px 11px}
.subscribe{position:absolute;left:328px;top:117px;width:85px;height:24px;border-radius:12px;background:var(--orange);color:#fff;font-size:10.5px;font-weight:500;text-align:center;line-height:24px}
.footer-brand{position:absolute;left:598px;top:30px;display:flex;flex-direction:column;align-items:center;gap:22px;width:132px}
.footer-brand span{width:56px;height:56px;border-radius:50%;background:#8f8f8f}
.footer-brand b{font-size:15px;font-weight:500;color:#bbb;white-space:nowrap}
.footer-bottom{position:absolute;top:185px;left:0;width:793px;height:1px;background:#4a4a4a}
.copyright{position:absolute;left:49px;top:199px;font-size:9px;color:#ccc}
.social{position:absolute;right:49px;top:194px;display:flex;gap:5px}
.social span{width:20px;height:20px;border-radius:50%;background:#8d8d8d}
</style>
</head>
<body>
<header class="site-header">
  <div class="brand-badge" aria-label="Meadowbrook Holdings"><span></span></div>
  <nav class="main-nav"><span>HOME</span><span>ASPIRING FARMERS</span><span>INVESTORS</span><span>RETIRING FARMER</span><span>BLOG</span><span>PRICING</span><span>CONTACT</span></nav>
  <div class="sign-in"><svg width="10" height="10" viewBox="0 0 10 10" fill="none" stroke="#f5890f" stroke-width="1.2"><path d="M4 1h5v8H4M1 5h5M4 3l2 2-2 2"/></svg>SIGN IN OR SIGN UP</div>
</header>
<section class="hero" role="img" aria-label="Photo of a farming family and a young farmer outdoors among trees"><h1>Farmer Profile</h1></section>
<div class="breadcrumb"><a>Home</a> / Farmer Profile</div>

<div class="profile-photo" role="img" aria-label="Profile photo of a kangaroo"></div>
<div class="profile-info">
  <h2>Sam Doyle</h2>
  <div class="field">Closest town you live next to:</div>
  <div class="field">State: <span>ACT</span></div>
  <div class="field">Areas you want to farm: <span>Canberra, North East NSW, Tasmania</span></div>
  <div class="field">Current Job: <span>Shearer</span></div>
  <div class="field">Past Job: <span>None</span></div>
  <div class="field">Years Experience: <span>0-1 Years</span></div>
</div>
<div class="divider" style="top:479px"></div>

<div class="col" style="left:49px">
  <h3>Farming Preferences:</h3>
  <ul>
    <li>Sheep <i class="badge">1</i></li><li>Beef <i class="badge">1</i></li><li>Market garden <i class="badge">1</i></li><li>Other livestock <i class="badge">1</i></li><li>Chickens <i class="badge">1</i></li><li>Specialty Crops <i class="badge">1</i></li><li>Dairy <i class="badge">1</i></li><li>Broad Acre Cropping <i class="badge">1</i></li><li>Goats <i class="badge">1</i></li><li>Viticulture <i class="badge">1</i></li>
  </ul>
  <div class="field other">Other Farming Preferences: <span>None</span></div>
</div>
<div class="col" style="left:286px">
  <h3>Farming Skills:</h3>
  <ul>
    <li>Business Management <i class="badge">1</i></li><li>Livestock Mustering <i class="badge">1</i></li><li>Human Resources <i class="badge">1</i></li><li>Marketing <i class="badge">1</i></li><li>Sales <i class="badge">1</i></li><li>Book Keeping <i class="badge">1</i></li><li>Machinery Operation <i class="badge">1</i></li><li>Planning <i class="badge">1</i></li><li>Fencing <i class="badge">1</i></li><li>Accounting <i class="badge">1</i></li><li>Cropping <i class="badge">1</i></li><li>Animal Husbandry <i class="badge">1</i></li><li>Agronomy <i class="badge">1</i></li>
  </ul>
  <div class="field other">Other Farming Skills: <span>None</span></div>
</div>
<div class="col" style="left:524px">
  <h3>Farming Methods:</h3>
  <ul>
    <li>Grass fed <i class="badge">1</i></li><li>Conventional <i class="badge">1</i></li><li>Organic <i class="badge">1</i></li><li>Byodynamic <i class="badge">1</i></li><li>Regenerative <i class="badge">1</i></li><li>Permaculture <i class="badge">1</i></li>
  </ul>
  <div class="field other">Other Farming Methods: <span>None</span></div>
</div>
<div class="divider" style="top:840px"></div>

<div class="options">
  <div class="field">Farming Options: <span>Share Farm</span></div>
  <div class="field">What have you been doing to get farm ready?</div>
  <div class="field">Why are you farming_dreamate about farming? <span>I love to work hard and get a sweat up under the Australian Sun</span></div>
  <div class="field">Your Dream Farm <span>I love to work hard and get a sweat up under the Australian Sun</span></div>
</div>

<footer class="footer">
  <h4 style="left:47px">From The Blog</h4>
  <div class="post" style="top:52px"><div class="date"><b>24</b>APR 17</div><p>Out of the Griddle House into the fire of soil health | Tom Reyes<small>Posted by Tom Reyes</small></p></div>
  <div class="post" style="top:118px"><div class="date"><b>21</b>APR 17</div><p>Harrison is a cool name, so is Mia, but their passion for farming<small>Posted by Harrison and Mia</small></p></div>
  <div class="vline" style="left:298px"></div>
  <div class="newsletter">
    <h4 style="left:327px">Subscribe To Our Newsletter</h4>
    <p>Want to be the first to know about our amazing discount offer?</p>
    <div class="email">Email Address</div>
    <div class="subscribe">Subscribe</div>
  </div>
  <div class="vline" style="left:573px"></div>
  <div class="footer-brand"><span></span><b>Meadowbrook Holdings</b></div>
  <div class="footer-bottom"></div>
  <div class="copyright">©2017 Meadowbrook Holdings. Terms of Use | Privay | Sitemap | Donate</div>
  <div class="social" aria-label="Social links"><span></span><span></span><span></span></div>
</footer>
</body>
</html>
```